Cleaning Bochure for Different Services

We need to create preferably an A4 brochure for cleaning services so we are able to give to our customers upon meeting them. check out our website for more info. It is www.brightvaleservices.co.uk We need a page on;-Commercial Cleaning-Carpet Cleaning-Oven Cleaning with description and some imagery.

Target Market(s)

Commercial Cleaning Customers

Industry/Entity Type

Office Cleaning

Font styles to use
Sans Serif

Colors
33a6d7
aaaaaa

Requirements
Must have
• 4 pages each containing these services
• -Commercial Cleaning (most important)
• -Carpet Cleaning
• -Oven Cleaning
Nice to have
• Clean and smart looking design use some imagination and possibly go wild!
• Must be eye catching!

```html
<!DOCTYPE html>
<html lang="en">
<head>
<meta charset="utf-8">
<title>Brightvale Cleaning – Service Brochure</title>
<link rel="stylesheet" href="https://fonts.googleapis.com/css2?family=Montserrat:wght@600;800&family=Open+Sans:wght@400;600&display=swap">
<style>
  :root{
    --brand-blue:#33a6d7;
    --brand-grey:#aaaaaa;
    --ink:#3a3f44;
    --muted:#7d8489;
    --paper:#ffffff;
    --backdrop:#eef1f3;
    --rule:#dfe3e6;
  }
  *{box-sizing:border-box;margin:0;padding:0}
  html,body{width:900px;height:1200px;overflow:hidden;background:var(--backdrop)}
  body{font-family:"Open Sans",Arial,sans-serif;color:var(--ink)}
  .spread{display:grid;grid-template-columns:410px 410px;grid-template-rows:580px 580px;gap:20px;padding:10px 30px}
  .page{background:var(--paper);position:relative;overflow:hidden;box-shadow:0 2px 8px rgba(0,0,0,.12)}
  .heading{font-family:"Montserrat",Arial,sans-serif;font-weight:800;color:var(--brand-blue);text-transform:uppercase;letter-spacing:-.5px;line-height:1}
  .heading .muted{color:var(--ink)}
  .body-text{font-size:7.5px;line-height:1.6;color:var(--muted);margin-bottom:7px}
  .photo{position:absolute}
  .page-footer{position:absolute;left:24px;right:24px;bottom:12px;border-top:1px solid var(--rule);padding-top:5px;font-size:6.5px;color:var(--muted);text-align:center}

  /* cover */
  .brand{position:absolute;left:26px;top:22px;display:flex;align-items:center;gap:6px;font-family:"Montserrat",Arial,sans-serif;font-weight:800;font-size:15px;color:var(--brand-blue)}
  .brand-dot{width:12px;height:12px;border-radius:50%;background:var(--brand-blue)}
  .cover-intro{position:absolute;left:26px;right:26px;top:72px;text-align:center}
  .cover-kicker{font-family:"Montserrat",Arial,sans-serif;font-weight:600;font-size:11px;color:var(--ink)}
  .cover-title{font-size:34px;margin:6px 0 10px}
  .cover-photo{left:0;right:0;top:170px;bottom:34px;background:linear-gradient(160deg,#f4f6f7 0%,#cfe0e7 45%,#7ea36b 100%)}

  /* commercial */
  .commercial-photo{left:0;right:0;top:0;height:255px;background:linear-gradient(180deg,#dfe9ee 0%,#bfd0d8 60%,#e9eef0 100%)}
  .section-head{position:absolute;left:0;right:0;display:flex;align-items:center;gap:8px}
  .section-head .bar{height:22px;flex:1;background:var(--brand-grey);opacity:.35}
  .commercial-head{top:270px}
  .commercial-head .heading{font-size:26px;padding-right:24px}
  .commercial-copy{position:absolute;left:24px;right:24px;top:306px}
  .feature-row{position:absolute;left:24px;right:24px;display:flex;justify-content:space-around;border-top:1px solid var(--rule);padding-top:10px}
  .feature{display:flex;flex-direction:column;align-items:center;gap:4px;font-size:6.5px;color:var(--ink);font-weight:600}
  .feature svg{width:20px;height:20px}
  .commercial-features{top:440px}

  /* carpet */
  .carpet-head{top:26px;padding-left:24px}
  .carpet-head .heading{font-size:19px}
  .carpet-copy{position:absolute;left:24px;right:24px;top:60px}
  .carpet-features{top:130px;left:24px;right:170px;border-top:none;justify-content:flex-start;gap:22px;flex-wrap:wrap}
  .carpet-photo{left:0;right:0;top:200px;bottom:34px;background:linear-gradient(180deg,#f3f5f6 0%,#d6dbde 50%,#8f9aa1 100%)}
  .booking-note{position:absolute;left:24px;top:250px;width:150px;background:rgba(255,255,255,.85);border-left:3px solid var(--brand-blue);padding:8px 9px}
  .booking-note .body-text{color:var(--ink)}

  /* oven */
  .oven-photo{right:0;top:0;width:250px;height:200px;background:linear-gradient(200deg,#c7cbcd 0%,#7c8489 60%,#4c5358 100%)}
  .oven-title{position:absolute;left:24px;top:40px}
  .oven-title .heading{font-size:34px}
  .oven-title .heading .muted{display:block;font-size:20px;letter-spacing:0}
  .oven-copy{position:absolute;left:24px;right:24px;top:214px}
  .subhead{font-family:"Montserrat",Arial,sans-serif;font-weight:600;font-size:9px;color:var(--ink);margin-bottom:5px}
  .oven-detail-photo{left:24px;width:170px;height:78px;background:linear-gradient(135deg,#3a3f44 0%,#e7c84a 70%,#f1d75b 100%)}
  .price-table{position:absolute;left:210px;right:24px;top:310px;border-collapse:collapse;font-size:7px}
  .price-table th{background:var(--brand-blue);color:#fff;text-align:left;padding:4px 6px;font-weight:600}
  .price-table td{padding:4px 6px;border-bottom:1px solid var(--rule);color:var(--ink)}
  .price-table td:last-child{text-align:right}
</style>
</head>
<body>
<main class="spread">

  <!-- Page 1: cover -->
  <section class="page cover">
    <div class="brand"><span class="brand-dot"></span>Brightvale Cleaning</div>
    <div class="cover-intro">
      <p class="cover-kicker">Paying too much for your bills? Why not try</p>
      <h1 class="heading cover-title">Brightvale Cleaning?</h1>
      <p class="body-text">We provide reliable cleaning for offices, shops and homes across the region. Our trained team works around your hours so your space is always ready.</p>
    </div>
    <div class="photo cover-photo" role="img" aria-label="Two uniformed cleaners vacuuming and dusting a bright office"></div>
    <p class="page-footer">Call 01234 567890 · www.brightvaleservices.co.uk</p>
  </section>

  <!-- Page 2: commercial cleaning -->
  <section class="page commercial">
    <div class="photo commercial-photo" role="img" aria-label="Cleaner mopping a glass-walled office corridor"></div>
    <div class="section-head commercial-head">
      <span class="bar"></span>
      <h2 class="heading">Commercial <span class="muted">Cleaning</span></h2>
    </div>
    <div class="commercial-copy">
      <p class="body-text">Our commercial team keeps offices, receptions and shared spaces spotless with flexible daily, weekly or one-off visits.</p>
      <p class="body-text">Every visit follows a clear checklist, so standards stay high and nothing is missed from desks to kitchens.</p>
      <p class="body-text">We use safe, eco-friendly products and fully insured staff you can trust with keys and alarms.</p>
    </div>
    <div class="feature-row commercial-features">
      <div class="feature"><svg viewBox="0 0 20 20" fill="none" stroke="var(--brand-blue)" stroke-width="1.6"><path d="M10 2l6 3v5c0 4-3 6.5-6 8-3-1.5-6-4-6-8V5z"/><path d="M7 10l2 2 4-4"/></svg>Fully insured staff</div>
      <div class="feature"><svg viewBox="0 0 20 20" fill="none" stroke="var(--brand-blue)" stroke-width="1.6"><circle cx="10" cy="10" r="8"/><path d="M10 5v5l3 2"/></svg>Flexible schedules</div>
      <div class="feature"><svg viewBox="0 0 20 20" fill="none" stroke="var(--brand-blue)" stroke-width="1.6"><path d="M4 16c0-8 5-12 12-12 0 7-4 12-12 12z"/><path d="M4 16l7-7"/></svg>Eco-friendly products</div>
    </div>
    <p class="page-footer">Call 01234 567890 · www.brightvaleservices.co.uk</p>
  </section>

  <!-- Page 3: carpet cleaning -->
  <section class="page carpet">
    <div class="section-head carpet-head">
      <h2 class="heading">Commercial <span class="muted">Carpet Cleaning</span></h2>
      <span class="bar"></span>
    </div>
    <div class="carpet-copy">
      <p class="body-text">Deep carpet cleaning lifts dirt, stains and allergens from high traffic areas without long drying times.</p>
      <p class="body-text">Our machines reach deep into fibres to restore colour and keep carpets fresh for longer.</p>
    </div>
    <div class="feature-row carpet-features">
      <div class="feature"><svg viewBox="0 0 20 20" fill="none" stroke="var(--brand-blue)" stroke-width="1.6"><circle cx="10" cy="10" r="8"/><path d="M6 10l3 3 5-6"/></svg>Stain removal</div>
      <div class="feature"><svg viewBox="0 0 20 20" fill="none" stroke="var(--brand-blue)" stroke-width="1.6"><rect x="3" y="3" width="14" height="14" rx="2"/><path d="M7 10h6M10 7l3 3-3 3"/></svg>Fast drying</div>
      <div class="feature"><svg viewBox="0 0 20 20" fill="none" stroke="var(--brand-blue)" stroke-width="1.6"><circle cx="10" cy="10" r="8"/><path d="M6 12c2-3 6-3 8 0"/></svg>Odour control</div>
    </div>
    <div class="photo carpet-photo" role="img" aria-label="Technician running a carpet cleaning machine across an office floor"></div>
    <div class="booking-note">
      <p class="body-text">Booking is simple. Call us or visit our website to arrange a free survey and quote for your premises.</p>
      <p class="body-text">We work evenings and weekends to avoid any disruption to your business.</p>
    </div>
    <p class="page-footer">Call 01234 567890 · www.brightvaleservices.co.uk</p>
  </section>

  <!-- Page 4: oven cleaning -->
  <section class="page oven">
    <div class="photo oven-photo" role="img" aria-label="Gloved hand cleaning the inside of an oven"></div>
    <div class="oven-title">
      <h2 class="heading">Oven <span class="muted">Cleaning</span></h2>
    </div>
    <div class="oven-copy">
      <p class="subhead">Ovens, hobs and extractors</p>
      <p class="body-text">Built up grease and burnt food are removed with a safe, fume-free process that leaves your oven like new.</p>
      <p class="body-text">Most ovens are cleaned in around two hours and ready to use straight away.</p>
    </div>
    <div class="photo oven-detail-photo" style="top:310px" role="img" aria-label="Yellow-gloved hands scrubbing an oven tray"></div>
    <div class="photo oven-detail-photo" style="top:396px" role="img" aria-label="Sparkling clean oven door and hob"></div>
    <table class="price-table">
      <thead><tr><th>Service</th><th>From</th></tr></thead>
      <tbody>
        <tr><td>Single oven</td><td>£45</td></tr>
        <tr><td>Double oven</td><td>£65</td></tr>
        <tr><td>Range cooker</td><td>£85</td></tr>
        <tr><td>Hob</td><td>£20</td></tr>
        <tr><td>Extractor</td><td>£20</td></tr>
      </tbody>
    </table>
    <p class="page-footer">Call 01234 567890 · www.brightvaleservices.co.uk</p>
  </section>

</main>
</body>
</html>
```